KM Rivergate Fitness personal training needs a new Business Card design for 2016

Business Card design:
Our current business card is very plain
We are bringing on our first team member next year and thought its a perfect time to have a new face lift for our company!

We are a Personal Training business "KM Rivergate Fitness" who specializes in strength and conditioning / weightloss training,
We also run a yearly Bootcamp called "Thunderpeak Bootcamps", this is our Logo Design which we are looking for

The pink and blue in the logo are our business colours, how ever we don't want those colours to heavily dominate the card.

We are looking for a business card which is eye catching, and creative.

I am open to suggestions and any designs :)

Logo Design:

For our Logo Design we are looking for a bright, energetic logo, preferably a word logo which portrays strength and high intensity
If it has icon's etc in it thats fine again im open for suggestions :)
The Logo Design is for our Bootcamp which runs yearly
The bootcamp is called "Thunderpeak Bootcamp"

Target Market(s)

Age 20-40
Individuals who want to look great and have more energy

Industry/Entity Type

Business

Contact Information for Business Card

On the front
KM Rivergate Fitness Kemal Mortby Personal Training / Bootcamps / Pilates / Nutrition Healthy mind, Healthy body, Stronger lifestyle < our slogan
Icons for the following
Email:
Mobile:
Facebook:
Instagram:

On the back we would like to include somewhere
"Show this card to receive 50% off your first 30min pt session"
"Valid to one user only"

Logo Text

Thunderpeak Bootcamp

Font styles to use
Serif

Colors
e34197
0255a3
000000
ffffff

Requirements
Must have
• - Icons for instagram, facebook, email and mobile phone
• - Slogan: Healthy mind, Healthy body, Stronger lifestyle
• - What we offer: Personal Training , Bootcamps, Pilates, Nutrition
• - Logo
Nice to have
• - Our 50% offer on the back
• - a place for a photo
Should not have
• - Pink and Blue everywhere

```html
<!DOCTYPE html>
<html lang="en">
<head>
<meta charset="utf-8">
<title>KM Rivergate Fitness – Business Card</title>
<link href="https://fonts.googleapis.com/css2?family=Saira:wght@400;500;600;700&display=swap" rel="stylesheet">
<style>
  :root {
    --brand-blue: #1c5fae;
    --brand-pink: #e34197;
    --ink: #222222;
    --ink-soft: #444444;
    --paper: #ffffff;
    --backdrop: #5b5b5b;
  }
  * { box-sizing: border-box; margin: 0; padding: 0; }
  html, body { width: 1105px; height: 1200px; overflow: hidden; }
  body {
    background: var(--backdrop);
    font-family: "Saira", sans-serif;
    position: relative;
  }
  .card {
    position: absolute;
    left: 196px;
    width: 720px;
    height: 412px;
    background: var(--paper);
    border-radius: 19px;
    overflow: hidden;
  }
  .card--front { top: 146px; }
  .card--back { top: 602px; }

  /* Front */
  .brand-mark {
    position: absolute;
    left: 118px; top: 53px;
    width: 84px; height: 84px;
    border-radius: 50%;
    background: var(--brand-blue);
  }
  .brand-name {
    position: absolute;
    left: 30px; top: 148px;
    width: 260px;
    text-align: center;
    line-height: 1;
  }
  .brand-name__main {
    display: block;
    color: var(--brand-blue);
    font-weight: 700;
    font-size: 31px;
  }
  .brand-name__sub {
    display: block;
    color: var(--brand-pink);
    font-weight: 700;
    font-size: 18px;
    letter-spacing: 3px;
    margin-top: 3px;
  }
  .accent-bar {
    position: absolute;
    width: 11px;
  }
  .accent-bar--left { left: 0; top: 236px; height: 133px; background: var(--brand-blue); }
  .accent-bar--right { right: 0; top: 276px; height: 47px; background: var(--brand-pink); }

  .contact-list {
    position: absolute;
    left: 46px; top: 235px;
    list-style: none;
  }
  .contact-list__item {
    display: flex;
    align-items: center;
    height: 27.6px;
    font-size: 19px;
    color: var(--ink);
  }
  .contact-list__icon {
    width: 18px; height: 18px;
    margin-right: 13px;
    flex: none;
  }
  .contact-list__icon--plain {
    background: var(--brand-blue);
    border-radius: 3px;
    width: 16px; height: 16px;
    margin-left: 1px; margin-right: 14px;
  }

  .person {
    position: absolute;
    right: 41px; top: 271px;
    text-align: right;
    line-height: 1;
  }
  .person__name {
    color: var(--brand-blue);
    font-weight: 600;
    font-size: 24px;
    letter-spacing: 0.5px;
  }
  .person__role {
    color: var(--brand-pink);
    font-size: 19px;
    margin-top: 9px;
  }

  /* Back */
  .back-disc {
    position: absolute;
    left: -72px; top: -1px;
    width: 414px; height: 414px;
    border-radius: 50%;
    background: var(--brand-blue);
  }
  .offer {
    position: absolute;
    right: 136px; top: 38px;
    text-align: right;
    color: var(--ink-soft);
    font-size: 17px;
    line-height: 23px;
  }
  .offer__lead { font-weight: 600; }
  .offer-badge {
    position: absolute;
    left: 594px; top: 28px;
    width: 94px; height: 94px;
  }
  .offer-badge__label {
    position: absolute;
    inset: 0;
    display: flex;
    flex-direction: column;
    align-items: center;
    justify-content: center;
    color: var(--paper);
    font-weight: 600;
    line-height: 0.95;
  }
  .offer-badge__value { font-size: 27px; }
  .offer-badge__unit { font-size: 25px; }

  .back-brand {
    position: absolute;
    left: 330px; top: 272px;
    width: 350px;
    text-align: center;
    line-height: 1;
  }
  .back-brand__main {
    display: block;
    color: var(--brand-blue);
    font-weight: 700;
    font-size: 38px;
  }
  .back-brand__sub {
    display: block;
    color: var(--brand-pink);
    font-weight: 700;
    font-size: 22px;
    letter-spacing: 4px;
    margin-top: 2px;
  }
  .services {
    position: absolute;
    left: 300px; top: 341px;
    width: 410px;
    text-align: center;
    color: var(--brand-blue);
    font-weight: 600;
    font-size: 16.5px;
    line-height: 22px;
    white-space: nowrap;
  }
  .slogan {
    position: absolute;
    left: 300px; top: 363px;
    width: 410px;
    text-align: center;
    color: var(--brand-pink);
    font-weight: 500;
    font-size: 16px;
    line-height: 22px;
    white-space: nowrap;
  }
</style>
</head>
<body>

<section class="card card--front" aria-label="Business card front">
  <div class="brand-mark"></div>
  <div class="brand-name">
    <span class="brand-name__main">KM RIVERGATE</span>
    <span class="brand-name__sub">FITNESS</span>
  </div>

  <div class="accent-bar accent-bar--left"></div>

  <ul class="contact-list">
    <li class="contact-list__item">
      <svg class="contact-list__icon" viewBox="0 0 18 18" aria-hidden="true">
        <rect x="4.5" y="1" width="9" height="16" rx="1.5" fill="none" stroke="#1c5fae" stroke-width="2"/>
        <rect x="7.5" y="13.5" width="3" height="1.5" fill="#1c5fae"/>
      </svg>
      614 208 7351
    </li>
    <li class="contact-list__item">
      <span class="contact-list__icon contact-list__icon--plain"></span>
      kmrivergate
    </li>
    <li class="contact-list__item">
      <span class="contact-list__icon contact-list__icon--plain"></span>
      kmrivergate
    </li>
    <li class="contact-list__item">
      <svg class="contact-list__icon" viewBox="0 0 18 18" aria-hidden="true">
        <rect x="1" y="4" width="16" height="11" fill="#1c5fae"/>
        <path d="M1 4 L9 10.5 L17 4" fill="none" stroke="#ffffff" stroke-width="1.5"/>
      </svg>
      hello@rivergatefit.com
    </li>
    <li class="contact-list__item">
      <svg class="contact-list__icon" viewBox="0 0 18 18" aria-hidden="true">
        <circle cx="9" cy="9" r="7.5" fill="#1c5fae"/>
        <ellipse cx="9" cy="9" rx="3.2" ry="7.5" fill="none" stroke="#ffffff" stroke-width="1"/>
        <line x1="1.5" y1="9" x2="16.5" y2="9" stroke="#ffffff" stroke-width="1"/>
      </svg>
      www.rivergatefit.com
    </li>
  </ul>

  <div class="person">
    <div class="person__name">KEMAL MORTBY</div>
    <div class="person__role">CEO/FOUNDER</div>
  </div>

  <div class="accent-bar accent-bar--right"></div>
</section>

<section class="card card--back" aria-label="Business card back">
  <div class="back-disc"></div>

  <div class="offer">
    <div class="offer__lead">Show this card to receive</div>
    <div class="offer__lead">your first 30min pt session</div>
    <div>Valid to one user only</div>
  </div>

  <div class="offer-badge">
    <svg viewBox="0 0 100 100" width="94" height="94" aria-hidden="true">
      <polygon fill="#1c5fae" points="100,50 92.47,56.73 97.55,65.45 88.31,69.52 90.45,79.39 80.41,80.41 79.39,90.45 69.52,88.31 65.45,97.55 56.73,92.47 50,100 43.27,92.47 34.55,97.55 30.48,88.31 20.61,90.45 19.59,80.41 9.55,79.39 11.69,69.52 2.45,65.45 7.53,56.73 0,50 7.53,43.27 2.45,34.55 11.69,30.48 9.55,20.61 19.59,19.59 20.61,9.55 30.48,11.69 34.55,2.45 43.27,7.53 50,0 56.73,7.53 65.45,2.45 69.52,11.69 79.39,9.55 80.41,19.59 90.45,20.61 88.31,30.48 97.55,34.55 92.47,43.27"/>
    </svg>
    <div class="offer-badge__label">
      <span class="offer-badge__value">50%</span>
      <span class="offer-badge__unit">off</span>
    </div>
  </div>

  <div class="back-brand">
    <span class="back-brand__main">KM RIVERGATE</span>
    <span class="back-brand__sub">FITNESS</span>
  </div>
  <div class="services">Personal Training | Bootcamps | Pilates | Nutrition</div>
  <div class="slogan">Healthy mind, Healthy body, Stronger lifestyle</div>
</section>

</body>
</html>
```